Maple Row Yardcare

I want it as prefession and attractive as possible we are a lawnmowing business

Phone number 605-318-2264
Name- Carl Whitby
Email- mapleroweyardsd@fernpost.net

```html
<!DOCTYPE html>
<html lang="en">
<head>
<meta charset="utf-8">
<title>Maple Row Yardcare – Business Card</title>
<link rel="stylesheet" href="https://fonts.googleapis.com/css2?family=Roboto+Condensed:wght@700&display=swap">
<style>
  :root {
    --bg: #242424;
    --forest: #0b5c36;
    --lime: #5cc04a;
    --paper: #ffffff;
    --ink-green: #0d5a33;
  }
  * { margin: 0; padding: 0; box-sizing: border-box; }
  html, body { width: 1175px; height: 1200px; overflow: hidden; background: var(--bg); }
  body { position: relative; font-family: "Roboto Condensed", "Arial Narrow", sans-serif; font-weight: 700; }

  .card {
    position: absolute;
    top: 463px;
    width: 482px;
    height: 274px;
    border-radius: 12px;
    overflow: hidden;
  }
  .card--front { left: 70px; background: var(--paper); }
  .card--back { left: 590px; background: var(--forest); }

  /* brand name lockup */
  .brand {
    position: absolute;
    display: flex;
    align-items: center;
    gap: 10px;
    text-transform: uppercase;
    letter-spacing: 0.5px;
    line-height: 1;
  }
  .brand__mark { width: 16px; height: 16px; background: currentColor; flex: none; }
  .card--front .brand { left: 26px; top: 40px; color: var(--ink-green); font-size: 30px; }
  .card--back .brand { left: 0; right: 0; top: 92px; justify-content: center; color: var(--paper); font-size: 38px; }

  .tagline {
    position: absolute;
    left: 24px;
    top: 118px;
    color: var(--ink-green);
    font-size: 15px;
    line-height: 20px;
    text-transform: uppercase;
  }

  .lawn-wave { position: absolute; inset: 0; width: 100%; height: 100%; }

  .contact {
    position: absolute;
    right: 24px;
    top: 188px;
    text-align: right;
    color: var(--paper);
  }
  .contact__phone { font-size: 28px; line-height: 32px; letter-spacing: 0.5px; }
  .contact__email { font-size: 14px; line-height: 18px; margin-top: 2px; }

  .mower-art {
    position: absolute;
    left: 76px;
    top: 196px;
    width: 118px;
    height: 72px;
    background: linear-gradient(180deg, #e9f3ec, #cfe3d5);
    border-radius: 6px;
    opacity: 0.9;
  }
  .grass-art {
    position: absolute;
    left: 200px;
    right: 0;
    top: 238px;
    height: 30px;
    background: linear-gradient(180deg, rgba(92,192,74,0), var(--lime));
  }
  .ground-line {
    position: absolute;
    left: 0; right: 0; bottom: 0;
    height: 6px;
    background: var(--lime);
  }
</style>
</head>
<body>

  <section class="card card--front" aria-label="Card front">
    <svg class="lawn-wave" viewBox="0 0 482 274" preserveAspectRatio="none" aria-hidden="true">
      <path fill="var(--forest)" d="M0 196 C40 218 90 236 150 222 C220 204 250 150 300 120 C350 92 400 100 440 104 C460 106 474 100 482 96 L482 274 L0 274 Z"/>
    </svg>
    <div class="brand"><span class="brand__mark"></span><span class="brand__name">Maple Row Yardcare</span></div>
    <p class="tagline">Weekly / Monthly<br>Scheduled Services</p>
    <div class="contact">
      <p class="contact__phone">605-318-2264</p>
      <p class="contact__email">mapleroweyardsd@fernpost.net</p>
    </div>
  </section>

  <section class="card card--back" aria-label="Card back">
    <div class="brand"><span class="brand__mark"></span><span class="brand__name">Maple Row Yardcare</span></div>
    <div class="mower-art" role="img" aria-label="White silhouette of a person pushing a lawn mower"></div>
    <div class="grass-art" role="img" aria-label="Bright green grass blades along the bottom edge"></div>
    <div class="ground-line"></div>
  </section>

</body>
</html>
```